Bright Orchard
Bright & Fun-filled
Talia Brennick
Certified Holistic Wellness Coach, NLP Practitioner
no address pls
talia@brightorchard.com
www.brightorchard.com
To love oneself is the beginning of a lifelong romance. --Edwin Tarrow

```html
<!DOCTYPE html>
<html lang="en">
<head>
<meta charset="utf-8">
<title>Bright Orchard — Business Card</title>
<link href="https://fonts.googleapis.com/css2?family=Dancing+Script:wght@500;600&family=Quicksand:wght@500&display=swap" rel="stylesheet">
<style>
  :root {
    --backdrop: #e4e4e6;
    --card: #ffffff;
    --pink: #e8336f;
    --pink-deep: #c81f58;
    --grey: #6b6b6b;
    --ink: #555555;
    --white: #ffffff;
  }
  * { margin: 0; padding: 0; box-sizing: border-box; }
  html, body { width: 1200px; height: 797px; overflow: hidden; }
  body {
    background: var(--backdrop);
    font-family: "Quicksand", sans-serif;
    position: relative;
  }
  .card {
    position: absolute;
    top: 256px;
    width: 500px;
    height: 286px;
    background: var(--card);
    border-radius: 10px;
    overflow: hidden;
    box-shadow: 0 10px 30px rgba(0,0,0,0.12);
  }
  .card--front { left: 70px; }
  .card--back { left: 630px; }

  .card__band { position: absolute; left: 0; bottom: 0; width: 100%; height: 120px; }

  .brand {
    display: flex;
    align-items: center;
    gap: 8px;
    font-family: "Dancing Script", cursive;
    font-weight: 600;
    color: var(--grey);
    white-space: nowrap;
  }
  .brand__dot { width: 14px; height: 14px; border-radius: 50%; background: var(--pink); }

  .card--front .brand {
    position: absolute; top: 92px; left: 0; width: 100%;
    justify-content: center; font-size: 46px;
  }
  .quote {
    position: absolute; left: 0; bottom: 28px; width: 100%;
    text-align: center; color: var(--white);
    font-family: "Dancing Script", cursive; font-weight: 500;
    font-size: 17px; line-height: 1.35;
  }
  .quote__author { display: block; padding-left: 140px; }

  .card__panel { position: absolute; left: 0; top: 0; height: 100%; width: 260px; }
  .identity {
    position: absolute; left: 18px; top: 118px; width: 230px;
    color: var(--white); text-align: center;
  }
  .identity__name { font-family: "Dancing Script", cursive; font-weight: 600; font-size: 30px; line-height: 1.1; }
  .identity__role { font-size: 7.5px; margin-top: 6px; letter-spacing: 0.2px; }

  .card--back .brand {
    position: absolute; top: 66px; right: 30px; font-size: 30px;
  }
  .contacts {
    position: absolute; right: 28px; top: 132px; width: 200px;
    list-style: none; color: var(--ink); font-size: 11px;
  }
  .contacts li { display: flex; align-items: center; gap: 10px; height: 26px; }
  .contacts svg { width: 12px; height: 12px; flex: none; }
</style>
</head>
<body>

  <section class="card card--front" aria-label="Card front">
    <div class="brand"><span class="brand__name">Bright Orchard</span><span class="brand__dot"></span></div>
    <svg class="card__band" viewBox="0 0 500 120" preserveAspectRatio="none" aria-hidden="true">
      <path d="M0 30 Q250 -10 500 30 L500 120 L0 120 Z" fill="#9a9a9a" opacity="0.35"/>
      <path d="M0 40 Q250 0 500 40 L500 120 L0 120 Z" fill="var(--pink)"/>
    </svg>
    <p class="quote">“To love oneself is the beginning of a lifelong romance.”
      <span class="quote__author">-- Edwin Tarrow --</span></p>
  </section>

  <section class="card card--back" aria-label="Card back">
    <svg class="card__panel" viewBox="0 0 260 286" preserveAspectRatio="none" aria-hidden="true">
      <path d="M0 0 L150 0 Q250 40 240 140 Q230 230 120 286 L0 286 Z" fill="var(--pink)"/>
    </svg>
    <div class="identity">
      <p class="identity__name">Talia Brennick</p>
      <p class="identity__role">Certified Holistic Wellness Coach, NLP Practitioner</p>
    </div>
    <div class="brand"><span class="brand__name">Bright Orchard</span><span class="brand__dot"></span></div>
    <ul class="contacts">
      <li><svg viewBox="0 0 12 12" aria-hidden="true"><circle cx="6" cy="6" r="6" fill="var(--pink)"/><rect x="4" y="3" width="4" height="6" rx="1" fill="var(--white)"/></svg>555.010.000</li>
      <li><svg viewBox="0 0 12 12" aria-hidden="true"><circle cx="6" cy="6" r="6" fill="var(--pink)"/><rect x="3" y="4" width="6" height="4" fill="var(--white)"/><path d="M3 4 L6 6.5 L9 4" stroke="var(--pink)" stroke-width="0.8" fill="none"/></svg>talia@brightorchard.com</li>
      <li><svg viewBox="0 0 12 12" aria-hidden="true"><circle cx="6" cy="6" r="6" fill="var(--pink)"/><circle cx="6" cy="6" r="3" fill="none" stroke="var(--white)" stroke-width="0.9"/><path d="M3 6 H9 M6 3 V9" stroke="var(--white)" stroke-width="0.7"/></svg>www.brightorchard.com</li>
    </ul>
  </section>

</body>
</html>
```